Popup Nightclub Grand Opening Flyer

We need to design a flyer for the grand opening of an upscale, exclusive nightclub called "Lanternfall". The design needs to be chic and exclusive. The background should be black and the text should primarily be white. We like minimalist designs.

Here is the text for the flyer
-
Velvetrope Atlanta Presents

Lanternfall (LOGO)

A Popup Nightclub Experience
For one night Only

Friday, October 18, 2013
Party begins at 9PM

INVITE ONLY

See invitation for location details
(Velvetrope Atlanta logo)

-
Examples we like

http://cdn2-b.brivelpost.com/sites/default/files/styles/image_content_width/hash/3d/fa/1472093815_4471_flyer.jpg?itok=R8kqWm2z

http://api.plovra.com/files/7Kqq-Tr82XXB3pQzJvmtR5HL2W719E4nbRtC6KLd4HsfM8Y2qTDK-VmjwDoNqLX4QBzTHD9nakRbVx3m-Pfq8htc3MDTWr5p4/2zelSaturdays.jpg

http://quenmar.com/wp-content/uploads/yootheme/widgetkit/gallery/2zel/2zel-gen_vroom4-01.jpg

Hi All, one thing that we are seeing that we don't like is on over emphasis on the phrase "a popup nightclub experience" please don't make this the largest thing on the flyer

Target Market(s)

Target market is 25-35 year olds who are affluent (rich) and like luxury brands

Requirements
Must have
• Dark Background
Nice to have
• Velvetrope Logo on the bottom
Modern text that isn't curvy
Should not have
• Curved text

```html
<!DOCTYPE html>
<html lang="en">
<head>
<meta charset="utf-8">
<title>Lanternfall Nightclub – Velvetrope Atlanta</title>
<link rel="stylesheet" href="https://fonts.googleapis.com/css2?family=Jost:wght@300;400;500&display=swap">
<style>
  :root {
    --backdrop: #e6e6e6;
    --flyer-black: #000000;
    --text-white: #ffffff;
    --text-grey: #8f8f8f;
    --mark-silver: #c9c9c9;
  }
  * { margin: 0; padding: 0; box-sizing: border-box; }
  html, body {
    width: 1200px;
    height: 1000px;
    overflow: hidden;
    background: var(--backdrop);
    font-family: "Jost", "Helvetica Neue", Arial, sans-serif;
  }
  .flyer {
    position: absolute;
    left: 282px;
    top: 18px;
    width: 680px;
    height: 962px;
    background: var(--flyer-black);
    color: var(--text-white);
    text-align: center;
  }
  .flyer p, .flyer h1, .flyer h2 {
    position: absolute;
    left: 0;
    width: 100%;
    font-weight: 300;
    line-height: 1;
  }
  .presenter { top: 40px; font-size: 21px; letter-spacing: 1.5px; color: var(--text-grey); }
  .club-mark { position: absolute; left: 280px; top: 128px; width: 120px; height: 120px; }
  .club-name { top: 336px; font-size: 66px; letter-spacing: 9px; padding-left: 9px; }
  .club-type { top: 428px; font-size: 33px; letter-spacing: 6px; padding-left: 6px; }
  .tagline { top: 564px; font-size: 23px; letter-spacing: 2px; }
  .tagline-note { top: 595px; font-size: 23px; letter-spacing: 2px; color: var(--text-grey); }
  .event-date { top: 655px; font-size: 23px; letter-spacing: 2px; }
  .event-time { top: 685px; font-size: 23px; letter-spacing: 2px; color: var(--text-grey); }
  .access { top: 758px; font-size: 23px; letter-spacing: 2.5px; }
  .location-note { top: 838px; font-size: 23px; letter-spacing: 2.5px; color: var(--text-grey); }
  .presenter-brand {
    position: absolute;
    left: 0;
    top: 882px;
    width: 100%;
    display: flex;
    justify-content: center;
    align-items: center;
    gap: 12px;
  }
  .presenter-brand .dot { width: 14px; height: 14px; border-radius: 50%; background: var(--text-white); }
  .presenter-brand .brand-name {
    font-size: 24px;
    font-weight: 400;
    letter-spacing: 3px;
    color: var(--text-white);
  }
</style>
</head>
<body>
  <main class="flyer">
    <p class="presenter">Velvetrope Atlanta Presents</p>

    <svg class="club-mark" viewBox="0 0 120 120" aria-hidden="true">
      <circle cx="60" cy="60" r="58" fill="var(--mark-silver)"/>
    </svg>

    <h1 class="club-name">LANTERNFALL</h1>
    <h2 class="club-type">NIGHTCLUB</h2>

    <p class="tagline">A Popup Nightclub Experience</p>
    <p class="tagline-note">For one night Only</p>

    <p class="event-date">Friday, October 18, 2013</p>
    <p class="event-time">Party begins at 9PM</p>

    <p class="access">INVITE ONLY</p>

    <p class="location-note">See invitation for location details</p>

    <div class="presenter-brand">
      <span class="dot"></span>
      <span class="brand-name">VELVETROPE ATLANTA</span>
    </div>
  </main>
</body>
</html>
```